KT Crewing business card

Require business card which includes:
Company name: KT CREWING PTY LTD
Email: Mick@ktcrewing.com.au
Phone: 0431 556 208
ACN: 517 238 649

slogan: Onsite Auto Electrician Labour hire

Details and logo on top side
Logo only on bottom side

colour codes : #F15A29 , #939598

Target Market(s)

Western Australia mining sector

Industry/Entity Type

Mining

Contact Information for Business Card

Require business card which includes: Company name: KT CREWING PTY LTD Email: Mick@ktcrewing.com.au Phone: 0431 556 208 ACN: 517 238 649 slogan: Onsite Auto Electrician Labour hire Details and logo on top side Logo only on bottom side colour codes : #F15A29 , #939598

Colors
EE7325
F08F49
F5BC92
FAE3D3
FDF4ED

Requirements
Must have
• double sided

```html
<!DOCTYPE html>
<html lang="en">
<head>
<meta charset="utf-8">
<title>KT Crewing – Business Card</title>
<link href="https://fonts.googleapis.com/css2?family=Questrial&display=swap" rel="stylesheet">
<style>
  :root {
    --brand-orange: #F15A29;
    --brand-orange-deep: #DE5125;
    --brand-grey: #939598;
    --ink: #3a3a3c;
    --paper: #FFFFFF;
    --paper-shade: #EDEDED;
    --stage: #2B2B2D;
  }
  * { box-sizing: border-box; margin: 0; padding: 0; }
  html, body {
    width: 1200px;
    height: 900px;
    overflow: hidden;
    background: var(--stage);
    font-family: "Questrial", "Century Gothic", sans-serif;
  }
  .stage {
    position: relative;
    width: 1200px;
    height: 900px;
  }
  .card {
    position: absolute;
    left: 290px;
    width: 620px;
    height: 379px;
    border-radius: 2px;
    box-shadow: 0 10px 28px rgba(0,0,0,0.45);
  }
  /* Back side – logo only */
  .card--back {
    top: 51px;
    background: linear-gradient(120deg, var(--brand-orange-deep), var(--brand-orange));
    display: flex;
    align-items: center;
    justify-content: center;
  }
  .brand-mark {
    display: flex;
    align-items: center;
    gap: 14px;
    font-size: 54px;
    line-height: 1;
    letter-spacing: 1px;
  }
  .brand-mark__square {
    width: 38px;
    height: 38px;
  }
  .card--back .brand-mark { color: var(--paper); }
  .card--back .brand-mark__square { background: var(--paper); }

  /* Front side – details and logo */
  .card--front {
    top: 470px;
    background: linear-gradient(115deg, var(--paper-shade) 0%, var(--paper) 70%);
  }
  .card--front .brand-mark {
    position: absolute;
    top: 54px;
    right: 50px;
    font-size: 46px;
    color: var(--brand-orange);
  }
  .card--front .brand-mark__square {
    width: 32px;
    height: 32px;
    background: var(--brand-grey);
  }
  .contact-row {
    position: absolute;
    right: 40px;
    bottom: 92px;
    display: flex;
    align-items: center;
    gap: 10px;
    font-size: 17px;
    color: var(--ink);
    white-space: nowrap;
  }
  .contact-item { display: flex; align-items: center; gap: 6px; }
  .contact-icon { width: 16px; height: 16px; fill: var(--brand-orange); }
  .contact-sep { color: var(--brand-grey); }
  .contact-label { color: var(--brand-orange); font-weight: 700; }
  .rule {
    position: absolute;
    left: 40px;
    right: 40px;
    bottom: 78px;
    height: 1.5px;
    background: var(--brand-orange);
  }
  .slogan {
    position: absolute;
    left: 40px;
    bottom: 40px;
    font-size: 21px;
    color: var(--ink);
    letter-spacing: 0.3px;
  }
</style>
</head>
<body>
<main class="stage">

  <section class="card card--back" aria-label="Business card back">
    <div class="brand-mark">
      <span class="brand-mark__square"></span>
      <span class="brand-mark__name">KT Crewing</span>
    </div>
  </section>

  <section class="card card--front" aria-label="Business card front">
    <div class="brand-mark">
      <span class="brand-mark__square"></span>
      <span class="brand-mark__name">KT Crewing</span>
    </div>

    <div class="contact-row">
      <span class="contact-item">
        <svg class="contact-icon" viewBox="0 0 24 24" aria-hidden="true">
          <path d="M6.6 10.8a15.1 15.1 0 0 0 6.6 6.6l2.2-2.2c.3-.3.7-.4 1-.2 1.1.4 2.3.6 3.6.6.6 0 1 .4 1 1V20c0 .6-.4 1-1 1C10.6 21 3 13.4 3 4c0-.6.4-1 1-1h3.5c.6 0 1 .4 1 1 0 1.3.2 2.5.6 3.6.1.3 0 .7-.2 1z"/>
        </svg>
        0431 556 208
      </span>
      <span class="contact-sep">|</span>
      <span class="contact-item">
        <svg class="contact-icon" viewBox="0 0 24 24" aria-hidden="true">
          <path d="M3 5h18c.6 0 1 .4 1 1v12c0 .6-.4 1-1 1H3c-.6 0-1-.4-1-1V6c0-.6.4-1 1-1zm9 7.2L20 7H4z"/>
        </svg>
        Mick@ktcrewing.com.au
      </span>
      <span class="contact-sep">|</span>
      <span class="contact-item">
        <span class="contact-label">ACN:</span> 517 238 649
      </span>
    </div>

    <div class="rule"></div>

    <p class="slogan">Onsite Auto Electrician Labour hire</p>
  </section>

</main>
</body>
</html>
```